Web Design For Manufacturing And Outsourcing Company

Pick up the pieces from our previous developer and help us complete our website.

5 pages - Home,Machining,Sourcing,About Us, and Contact

Attached you will find screen shots of previous direction but we're open to new ideas.

We can provide all text and images needed.

Thanks!

5+ page

```html
<!DOCTYPE html>
<html lang="en">
<head>
<meta charset="utf-8">
<title>Calder Industries</title>
<link href="https://fonts.googleapis.com/css2?family=Montserrat:wght@400;500;600;700&display=swap" rel="stylesheet">
<style>
:root{
  --orange:#f26a21;
  --ink:#333333;
  --muted:#555555;
  --grey:#5a5a5a;
  --panel:#f2f2f2;
  --navy:#1d3f73;
  --white:#ffffff;
  --black:#111111;
}
*{margin:0;padding:0;box-sizing:border-box}
html,body{width:1200px;height:4072px;overflow:hidden}
body{position:relative;font-family:'Montserrat',sans-serif;color:var(--ink);background:var(--white)}
.abs{position:absolute}
.site-header{position:absolute;left:0;top:0;width:1200px;height:87px;background:var(--white)}
.brand{left:114px;top:24px;display:flex;align-items:center;gap:12px;font-weight:700;font-size:17px;letter-spacing:2px;color:var(--ink)}
.brand-square{width:34px;height:38px;background:var(--orange)}
.main-nav{left:491px;top:32px;display:flex;gap:36px;font-size:15px;font-weight:500}
.header-phone{left:924px;top:21px;display:flex;align-items:center;gap:14px;font-size:15px}
.phone-dot{width:42px;height:42px;border-radius:50%;background:var(--orange);display:flex;align-items:center;justify-content:center}
.hero{left:0;top:87px;width:1200px;height:557px;background:linear-gradient(180deg,#c9b89a 0%,#8e7c60 40%,#4c4a3e 75%,#2f2d28 100%);border-bottom:3px dashed #fff}
.hero-title{left:0;top:240px;width:1200px;text-align:center;color:#fff;font-size:70px;font-weight:600;text-shadow:0 3px 8px rgba(0,0,0,.45)}
.hero-sub{left:260px;top:336px;width:680px;text-align:center;color:#fff;font-size:19px;line-height:30px;text-shadow:0 2px 6px rgba(0,0,0,.5)}
.btn{display:flex;align-items:center;justify-content:center;background:var(--orange);color:#fff;font-weight:600;border-radius:30px}
.hero-btn{left:508px;top:415px;width:184px;height:52px;font-size:16px}
.dot{width:14px;height:14px;border-radius:50%;background:#fff}
.dot-ring{left:1123px;top:325px;width:24px;height:24px;border:3px solid #fff;border-radius:50%;display:flex;align-items:center;justify-content:center}
.about-logo{left:166px;top:755px;width:288px;height:288px;border-radius:50%;border:22px solid var(--navy);display:flex;align-items:center;justify-content:center;font-size:34px;font-weight:700;color:var(--navy)}
.experience{left:182px;top:1082px;font-size:46px;font-weight:700;line-height:56px;color:var(--orange)}
.section-title{font-size:48px;font-weight:700;color:var(--orange)}
.section-sub{font-size:26px;font-weight:500;color:var(--grey)}
.body-text{font-size:15px;line-height:28px;color:var(--muted)}
.value-card{left:538px;width:548px;height:128px;border:2px solid #555;border-left:8px solid var(--orange);background:#fff}
.value-card svg{position:absolute;left:35px;top:34px}
.value-card h4{position:absolute;left:133px;top:22px;font-size:22px;font-weight:500;color:var(--grey)}
.value-card p{position:absolute;left:133px;top:60px;width:380px;font-size:13px;line-height:22px;color:var(--muted)}
.sourcing{left:0;top:1705px;width:1200px;height:858px;background:var(--panel);border-top:3px dashed #888;border-bottom:3px dashed #888}
.photo{background:linear-gradient(160deg,#6f9fd6 0%,#a9c3e0 45%,#f1b56a 70%,#4b3a2e 100%)}
.badge{width:190px;height:190px;border-radius:50%;border:19px solid var(--orange);background:#fff;display:flex;flex-direction:column;align-items:center;justify-content:center;gap:6px;font-size:18px;font-weight:600;color:var(--ink)}
.badge.grey{border-color:var(--grey)}
.machining-photo{background:linear-gradient(180deg,#b7ccdf,#6f7f8f 60%,#4a4740)}
.caption{left:130px;top:3172px;width:459px;text-align:center;color:#fff;font-size:28px;font-weight:600;text-shadow:0 2px 6px rgba(0,0,0,.5)}
.contact{left:0;top:3340px;width:1200px;height:610px;background:var(--panel)}
.field{border-bottom:2px solid #9a9a9a;font-size:19px;color:#888;padding-bottom:10px}
.site-footer{left:0;top:3950px;width:1200px;height:122px;background:var(--black)}
.social{width:26px;height:26px;border-radius:50%;border:2px solid #fff}
.copyright{left:0;top:4022px;width:1200px;text-align:center;color:#fff;font-size:14px}
</style>
</head>
<body>

<header class="site-header">
  <div class="abs brand"><span class="brand-square"></span><span>CALDER INDUSTRIES</span></div>
  <nav class="abs main-nav"><span>Home</span><span>Machining</span><span>Sourcing</span><span>Contact</span></nav>
  <div class="abs header-phone">
    <span class="phone-dot"><svg width="20" height="20" viewBox="0 0 24 24"><path d="M6.6 10.8a15 15 0 006.6 6.6l2.2-2.2c.3-.3.7-.4 1-.2 1.1.4 2.3.6 3.6.6.6 0 1 .4 1 1V20c0 .6-.4 1-1 1A17 17 0 013 4c0-.6.4-1 1-1h3.5c.6 0 1 .4 1 1 0 1.3.2 2.5.6 3.6.1.3 0 .7-.2 1z" fill="#fff"/></svg></span>
    <span>555 014-2290</span>
  </div>
</header>

<section class="abs hero" role="img" aria-label="Construction site with tower cranes against a forest at sunset"></section>
<h1 class="abs hero-title">Calder Industries</h1>
<p class="abs hero-sub">Founded by a third generation machine shop owner, obsessed with streamlining the manufacturing process from start to finish.</p>
<a class="abs btn hero-btn">Read More</a>
<div class="abs dot-ring"><span class="dot" style="width:12px;height:12px"></span></div>
<span class="abs dot" style="left:1128px;top:365px"></span>
<span class="abs dot" style="left:1128px;top:392px"></span>

<section>
  <div class="abs about-logo">Calder</div>
  <div class="abs experience">50 Years<br>Experience</div>
  <h2 class="abs section-title" style="left:538px;top:748px">About Us</h2>
  <h3 class="abs section-sub" style="left:538px;top:826px">Quality Policy</h3>
  <p class="abs body-text" style="left:538px;top:872px;width:548px;text-align:justify">We are committed to consistently exceeding customer expectations by providing products, services and sourcing solutions of the highest standard of quality. With our streamlined processes our method is efficient, provides value and ensures on time delivery. Our success is based on continuously improving the efficiencies and effectiveness of our products, processes, and quality management systems.</p>
  <h3 class="abs" style="left:538px;top:1080px;font-size:28px;font-weight:700">Core Values</h3>

  <div class="abs value-card" style="top:1143px">
    <svg width="60" height="60" viewBox="0 0 60 60" fill="none" stroke="#f26a21" stroke-width="2.5"><circle cx="30" cy="10" r="5"/><rect x="22" y="17" width="16" height="10"/><circle cx="14" cy="34" r="5"/><rect x="6" y="41" width="16" height="10"/><circle cx="46" cy="34" r="5"/><rect x="38" y="41" width="16" height="10"/></svg>
    <h4>Team Work</h4>
    <p>We are one company, one team. We understand when we work together we work smarter and not harder.</p>
  </div>
  <div class="abs value-card" style="top:1298px">
    <svg width="60" height="60" viewBox="0 0 60 60" fill="none" stroke="#f26a21" stroke-width="2.5"><path d="M30 50 10 32a10 10 0 0114-14l6 6 6-6a10 10 0 0114 14z"/><path d="M20 32l8 8M26 28l8 8"/></svg>
    <h4>Respect</h4>
    <p>We treat others as we expect to be treated, showing consideration for those around us.</p>
  </div>
  <div class="abs value-card" style="top:1455px">
    <svg width="60" height="60" viewBox="0 0 60 60" fill="none" stroke="#f26a21" stroke-width="2.5"><path d="M30 4l4 8 8 1-6 6 2 8-8-4-8 4 2-8-6-6 8-1z"/><circle cx="30" cy="38" r="5"/><path d="M14 36l16 18 16-18"/></svg>
    <h4>Gratitude</h4>
    <p>We appreciate where we have come from and the opportunities we are given to continue our journey.</p>
  </div>
</section>

<section class="abs sourcing"></section>
<h2 class="abs section-title" style="left:111px;top:1800px">Sourcing</h2>
<h3 class="abs section-sub" style="left:111px;top:1862px">Our In-house capabilities</h3>
<p class="abs body-text" style="left:111px;top:1912px;width:508px;font-size:14px">Over the years we identified the need to provide one stop services to purchasing departments. We have built an extensive network of hard to find products, machining specialists and leveraging open machine time to provide the most economical alternatives to our customers. We have developed a specialized method to supply our customers with the benefits they desire.</p>
<a class="abs btn" style="left:111px;top:2101px;width:182px;height:49px;font-size:15px">Read More</a>
<div class="abs" style="left:687px;top:1830px;width:421px;height:318px;background:var(--orange)"></div>
<div class="abs photo" style="left:668px;top:1811px;width:421px;height:320px" role="img" aria-label="Tower cranes over a building site against a sunlit blue sky"></div>

<div class="abs badge" style="left:177px;top:2294px">
  <svg width="56" height="48" viewBox="0 0 56 48" fill="none" stroke="#f26a21" stroke-width="2.5"><rect x="20" y="2" width="16" height="14"/><rect x="4" y="28" width="16" height="14"/><rect x="36" y="28" width="16" height="14"/><path d="M28 16v6M12 28v-6h32v6"/></svg>
  <span>Vetting</span>
</div>
<div class="abs badge grey" style="left:399px;top:2240px">
  <svg width="56" height="50" viewBox="0 0 56 50" fill="none" stroke="#333" stroke-width="3"><circle cx="26" cy="26" r="20"/><path d="M16 26l8 8 26-28"/></svg>
  <span>Quality</span>
</div>
<div class="abs badge" style="left:619px;top:2294px">
  <svg width="52" height="52" viewBox="0 0 52 52" fill="none" stroke="#f26a21" stroke-width="2.5"><rect x="6" y="4" width="34" height="42"/><path d="M12 14h10M12 22h20M12 30h14"/><circle cx="38" cy="38" r="9"/></svg>
  <span>Process</span>
</div>
<div class="abs badge grey" style="left:834px;top:2240px">
  <svg width="56" height="50" viewBox="0 0 56 50" fill="none" stroke="#333" stroke-width="2.5"><rect x="6" y="34" width="8" height="12"/><rect x="20" y="26" width="8" height="20"/><rect x="34" y="16" width="8" height="30"/><path d="M6 24l16-10 10 4 16-14M40 4h8v8"/></svg>
  <span>Benefits</span>
</div>

<section>
  <h2 class="abs section-title" style="left:0;top:2640px;width:1200px;text-align:center">Machining</h2>
  <h3 class="abs section-sub" style="left:0;top:2709px;width:1200px;text-align:center">Our In-house capabilities</h3>
  <p class="abs body-text" style="left:271px;top:2760px;width:660px;text-align:center;font-size:14px">Calder Industries brings their machining knowledge to the table every day working closely with our customers to put value into each part we produce. Working as a strategic partner, Calder Industries is able to deliver precision machined components with the highest quality, on time, and at the most cost effective price.</p>
  <div class="abs" style="left:130px;top:2897px;width:459px;height:340px;background:linear-gradient(180deg,#1f3657,#3c4d63 50%,#8a6b3d)" role="img" aria-label="Industrial overhead crane inside a large factory hall"></div>
  <div class="abs caption">Multiple Axis Equipment</div>
  <div class="abs machining-photo" style="left:600px;top:2897px;width:228px;height:163px" role="img" aria-label="Yellow mobile crane on a construction site"></div>
  <div class="abs machining-photo" style="left:839px;top:2897px;width:231px;height:163px;background:linear-gradient(180deg,#a7bfd8,#c9a36a 70%,#5b4c3c)" role="img" aria-label="Cranes at a site during sunset"></div>
  <div class="abs machining-photo" style="left:600px;top:3073px;width:228px;height:164px;background:linear-gradient(180deg,#cfd9e4,#9aa4ac 50%,#c99b2e)" role="img" aria-label="Yellow wheel loader on a work site"></div>
  <div class="abs machining-photo" style="left:839px;top:3073px;width:231px;height:164px;background:linear-gradient(180deg,#e6eef5,#c9d6e2 60%,#d7a95a)" role="img" aria-label="Worker in hard hat viewing a crane"></div>
</section>

<section class="abs contact"></section>
<h2 class="abs section-title" style="left:0;top:3408px;width:1200px;text-align:center">Contact Form</h2>
<div class="abs field" style="left:144px;top:3530px;width:912px;padding-left:14px">Your Email</div>
<div class="abs field" style="left:144px;top:3611px;width:429px;padding-left:14px">First Name</div>
<div class="abs field" style="left:627px;top:3616px;width:429px;padding-left:14px">Last Name</div>
<div class="abs field" style="left:144px;top:3692px;width:429px;padding-left:14px">Company Name</div>
<div class="abs field" style="left:627px;top:3699px;width:429px;padding-left:14px">Phone</div>
<a class="abs btn" style="left:497px;top:3806px;width:247px;height:55px;font-size:18px">Submit</a>

<footer class="abs site-footer"></footer>
<span class="abs social" style="left:533px;top:3981px"></span>
<span class="abs social" style="left:568px;top:3981px"></span>
<span class="abs social" style="left:606px;top:3981px"></span>
<span class="abs social" style="left:641px;top:3981px"></span>
<p class="abs copyright">© 2019 Copyrights | All Rights Reserved</p>

</body>
</html>
```